New, clean letterhead for law firm in Colorado using recently designed logo.

Professional letterhead for established law firm rebranding. We service high end clientele with mostly family law and personal injury cases. Need source files for future changes. Prefer logo at top, names of members and staff in left margin, contact info in footer.

Target Market(s)

High wealth individuals

Contact Information for Business Card

Need options for traditional and square two sided business cards

Font styles to use
Serif

Colors
0555a3

Requirements
Must have
• Our logo; blue, gray, and white; modern feel.
Should not have
• Images of people

```html
<!DOCTYPE html>
<html lang="en">
<head>
<meta charset="utf-8">
<title>Harlow Ridge Law, LLC — Letterhead</title>
<link rel="stylesheet" href="https://fonts.googleapis.com/css2?family=Encode+Sans+Condensed:wght@400&family=Lato:wght@400;700&display=swap">
<style>
  :root {
    --brand-blue: #1f64ad;
    --ink: #5b5b5b;
    --ink-soft: #666666;
    --paper: #ffffff;
    --backdrop: #d8d8d8;
    --signature-tone: #d6e3f2;
  }
  * { margin: 0; padding: 0; box-sizing: border-box; }
  html, body {
    width: 1056px;
    height: 1200px;
    overflow: hidden;
    background: var(--backdrop);
  }
  .letterhead {
    position: absolute;
    left: 104px;
    top: 0;
    width: 848px;
    height: 1200px;
    background: var(--paper);
  }
  .firm-name {
    position: absolute;
    left: 0;
    right: 0;
    top: 168px;
    text-align: center;
    font-family: "Lato", sans-serif;
    font-weight: 700;
    color: var(--brand-blue);
  }
  .firm-name__main {
    display: block;
    font-size: 28px;
    letter-spacing: 1.5px;
    line-height: 34px;
  }
  .firm-name__suffix {
    display: block;
    font-size: 19px;
    letter-spacing: 1px;
    line-height: 24px;
  }
  .letter-body {
    font-family: "Encode Sans Condensed", sans-serif;
    font-size: 17px;
    line-height: 29.5px;
    color: var(--ink);
  }
  .letter-body p {
    position: absolute;
    left: 79px;
    width: 688px;
    text-align: justify;
  }
  .salutation { top: 541px; }
  .para-1 { top: 597px; }
  .para-2 { top: 744px; }
  .para-3 { top: 862px; }
  .para-4 { top: 981px; }
  .closing { top: 1143px; }
  .salutation, .closing { text-align: left !important; }
  /* shift for base layout */
  .letter-body p { margin-top: -200px; }
  .signature {
    position: absolute;
    left: 75px;
    top: 968px;
    width: 68px;
    height: 44px;
    background: var(--signature-tone);
    border-radius: 4px;
  }
  .footer {
    position: absolute;
    left: 0;
    right: 0;
    top: 1113px;
  }
  .footer__title {
    display: flex;
    align-items: center;
    justify-content: center;
    gap: 14px;
    font-family: "Lato", sans-serif;
    font-weight: 700;
    font-size: 14px;
    letter-spacing: 3.4px;
    color: var(--brand-blue);
  }
  .footer__rule {
    width: 192px;
    height: 1px;
    background: var(--brand-blue);
  }
  .footer__contacts {
    margin-top: 10px;
    text-align: center;
    font-family: "Lato", sans-serif;
    font-size: 14.5px;
    color: var(--ink-soft);
    white-space: nowrap;
  }
  .footer__sep { margin: 0 6px; }
</style>
</head>
<body>
  <main class="letterhead">
    <header class="firm-name">
      <span class="firm-name__main">HARLOW RIDGE</span>
      <span class="firm-name__suffix">LAW, LLC</span>
    </header>

    <section class="letter-body">
      <p class="salutation">Dear Sir/Mam,</p>
      <p class="para-1">Contrary to popular belief, Lorem Ipsum is not simply random text. It has roots in a piece of classical Latin literature from 45 BC, making it over 2000 years old. Daniel Whitcombe, a Latin professor at Alder Grove College in Virginia, looked up one of the more obscure Latin words, consectetur.</p>
      <p class="para-2">Lorem Ipsum comes from sections 1.10.32 and 1.10.33 of "de Finibus Bonorum et Malorum" (The Extremes of Good and Evil) by Aurelian, written in 45 BC. This book is a treatise on the theory of ethics, very popular during the Renaissance. The first line of Lorem Ipsum.</p>
      <p class="para-3">The standard chunk of Lorem Ipsum used since the 1500s is reproduced below for those interested. Sections 1.10.32 and 1.10.33 from "de Finibus Bonorum et Malorum" by Aurelian are also reproduced in their exact original.</p>
      <p class="para-4">The standard chunk of Lorem Ipsum used since the 1500s is reproduced below for those interested.</p>
      <p class="closing">Best Regards</p>
    </section>

    <div class="signature" role="img" aria-label="Handwritten signature of the sender"></div>

    <footer class="footer">
      <div class="footer__title">
        <span class="footer__rule"></span>
        <span>HARLOW RIDGE LAW, LLC</span>
        <span class="footer__rule"></span>
      </div>
      <div class="footer__contacts">
        555-014-2290<span class="footer__sep">|</span>office@harlowridgelaw.com<span class="footer__sep">|</span>www.harlowridgelaw.com<span class="footer__sep">|</span>410 Larkspur Avenue #200 Denver, CO 80202
      </div>
    </footer>
  </main>
</body>
</html>
```